Looking for something outstanding

2 side business card, one side just the logo preferably the metallic 3D color or my original logo for uv printing. Be creative

Colors

Designer to choose colors to be used in the design.

Requirements
Must have
• Here my info for the business cards
• Owen Hardy
• President
• (555) 302-8816
• Owen@cobaltbuildgroup.com
• Office@cobaltbuildgroup.com
• www.cobaltbuildgroup.com
• FB @cobaltbuildgroup
• Dallas-Fort Worth

```html
<!DOCTYPE html>
<html lang="en">
<head>
<meta charset="utf-8">
<title>Cobalt Build Group – Business Card</title>
<link href="https://fonts.googleapis.com/css2?family=Roboto:wght@400;500&display=swap" rel="stylesheet">
<style>
  :root {
    --stage: #2e2e2e;
    --card-black: #161616;
    --card-white: #ffffff;
    --ink: #2a2a2a;
    --red: #e3262b;
    --blue: #3a3f9e;
    --steel: #5c5c5c;
  }
  * { box-sizing: border-box; margin: 0; padding: 0; }
  html, body {
    width: 1200px; height: 960px; overflow: hidden;
    background: var(--stage);
    font-family: "Roboto", Arial, sans-serif;
  }
  .stage {
    width: 1200px; height: 960px;
    display: flex; flex-direction: column;
    align-items: center; justify-content: center; gap: 60px;
  }
  .card {
    width: 700px; height: 400px;
    border-radius: 26px;
    position: relative;
    box-shadow: 0 10px 30px rgba(0,0,0,.45);
  }
  /* Back side */
  .card--back {
    background: var(--card-black);
    display: flex; align-items: center; justify-content: center;
  }
  .wordmark { display: flex; align-items: center; gap: 16px; }
  .wordmark__square { width: 46px; height: 46px; background: var(--steel); }
  .wordmark__name {
    font-weight: 500; font-size: 44px; letter-spacing: 4px;
    color: var(--steel); text-transform: uppercase;
  }
  /* Front side */
  .card--front { background: var(--card-white); }
  .front__logo {
    position: absolute; left: 54px; top: 40px;
    display: flex; align-items: center; gap: 12px;
  }
  .front__logo .wordmark__square { width: 30px; height: 30px; background: var(--red); }
  .front__logo .wordmark__name { font-size: 28px; letter-spacing: 2px; color: var(--red); }
  .holder { position: absolute; left: 54px; top: 98px; }
  .holder__name { font-size: 32px; font-weight: 400; letter-spacing: 1px; line-height: 1.2; }
  .holder__first { color: var(--red); }
  .holder__last { color: var(--blue); }
  .holder__title { font-size: 19px; color: var(--ink); margin-top: 2px; }
  .holder__rule { width: 66px; height: 2px; background: var(--red); margin-top: 10px; }
  .address { margin-top: 14px; font-size: 19px; line-height: 1.3; color: var(--ink); }
  .contacts { margin-top: 10px; list-style: none; font-size: 19px; color: var(--ink); }
  .contacts li { display: flex; align-items: center; gap: 12px; line-height: 1.38; }
  .contacts svg { width: 15px; height: 15px; flex: none; }
</style>
</head>
<body>
<main class="stage">
  <section class="card card--back" aria-label="Card back">
    <div class="wordmark">
      <span class="wordmark__square"></span>
      <span class="wordmark__name">Cobalt Build Group</span>
    </div>
  </section>

  <section class="card card--front" aria-label="Card front">
    <div class="front__logo wordmark">
      <span class="wordmark__square"></span>
      <span class="wordmark__name">Cobalt Build Group</span>
    </div>
    <div class="holder">
      <h1 class="holder__name"><span class="holder__first">OWEN</span> <span class="holder__last">HARDY</span></h1>
      <p class="holder__title">President</p>
      <div class="holder__rule"></div>
      <p class="address">Dallas-Fort Worth</p>
      <ul class="contacts">
        <li>
          <svg viewBox="0 0 16 16" aria-hidden="true"><path fill="#e3262b" d="M3.5 1.5l2.5 0 1 3.5-1.6 1.2a8 8 0 0 0 4.4 4.4l1.2-1.6 3.5 1v2.5c0 .8-.7 1.5-1.5 1.5A12 12 0 0 1 2 3c0-.8.7-1.5 1.5-1.5z"/></svg>
          (555) 302-8816
        </li>
        <li>
          <svg viewBox="0 0 16 16" aria-hidden="true"><rect x="1" y="3" width="14" height="10" fill="#e3262b"/><path d="M1 3l7 6 7-6" fill="none" stroke="#fff" stroke-width="1.4"/></svg>
          Owen@cobaltbuildgroup.com
        </li>
        <li>
          <svg viewBox="0 0 16 16" aria-hidden="true"><rect x="1" y="3" width="14" height="10" fill="#e3262b"/><path d="M1 3l7 6 7-6" fill="none" stroke="#fff" stroke-width="1.4"/></svg>
          Office@cobaltbuildgroup.com
        </li>
        <li>
          <svg viewBox="0 0 16 16" aria-hidden="true"><circle cx="8" cy="8" r="7" fill="#e3262b"/><path d="M1 8h14M8 1c-3 3-3 11 0 14M8 1c3 3 3 11 0 14" fill="none" stroke="#fff" stroke-width="1"/></svg>
          www.cobaltbuildgroup.com
        </li>
        <li>
          <svg viewBox="0 0 16 16" aria-hidden="true"><circle cx="8" cy="8" r="6" fill="#e3262b"/></svg>
          FB @cobaltbuildgroup
        </li>
      </ul>
    </div>
  </section>
</main>
</body>
</html>
```